Kolna Thai Massage Double Sided Flyer Luxury

I require a double sided flyer
we are a Thai Massage Spa
Would like gold, deep purple and bronze colours
Something eye catching and looks professional

```html
<!DOCTYPE html>
<html lang="en">
<head>
<meta charset="UTF-8">
<title>Kolna Thai Massage – Double Sided Flyer</title>
<link rel="stylesheet" href="https://fonts.googleapis.com/css2?family=Cinzel:wght@400;600&family=Muli:wght@400;700&family=Raleway:wght@400;700&display=swap">
<style>
  :root {
    --page: #ffffff;
    --brown: #2f1b12;
    --brown-soft: #3a2318;
    --gold: #e0a02c;
    --gold-deep: #e3951c;
    --yellow: #f3ea6e;
    --ink: #1a1008;
    --white: #ffffff;
    --skin-light: #e9c2a6;
    --skin-deep: #b27356;
  }
  * { margin: 0; padding: 0; box-sizing: border-box; }
  html, body { width: 896px; height: 1200px; overflow: hidden; background: var(--page); }
  body { position: relative; font-family: "Raleway", "Muli", sans-serif; }

  .flyer {
    position: absolute;
    top: 304px;
    width: 704px;
    height: 995px;
    transform: scale(0.594);
    transform-origin: top left;
    overflow: hidden;
    background: var(--brown);
  }
  .flyer--front { left: 20px; }
  .flyer--back { left: 458px; }

  .shapes { position: absolute; inset: 0; width: 100%; height: 100%; }

  .hero-photo {
    position: absolute; left: 0; top: 0; width: 704px; height: 540px;
    background: linear-gradient(135deg, var(--skin-light) 0%, #d79e7f 45%, var(--skin-deep) 100%);
  }

  .headline {
    position: absolute; left: 0; right: 0; top: 548px;
    text-align: center;
    font-family: "Cinzel", serif; font-weight: 400;
    color: var(--gold); font-size: 38px; line-height: 38px;
  }
  .intro {
    position: absolute; left: 114px; width: 476px;
    color: var(--white); font-size: 13px; line-height: 17px; text-align: center;
  }
  .intro--one { top: 631px; }
  .intro--two { top: 699px; }
  .intro--three { top: 799px; text-align: justify; text-align-last: center; }
  .section-title {
    position: absolute; left: 0; right: 0; top: 762px; text-align: center;
    font-family: "Cinzel", serif; color: var(--gold); font-size: 25px; line-height: 28px;
  }
  .voucher-front {
    position: absolute; left: 0; right: 0; top: 893px; text-align: center;
    font-family: "Cinzel", serif; color: var(--ink); font-size: 44px; line-height: 50px;
  }

  .back-title {
    position: absolute; left: 0; right: 0; top: 44px; text-align: center;
    font-family: "Cinzel", serif; color: var(--white); font-size: 34px; letter-spacing: 1px;
  }
  .treatment {
    position: absolute; left: 78px; width: 547px;
    border: 5px solid var(--gold);
  }
  .treatment--deep { top: 138px; height: 338px; }
  .treatment--thai { top: 534px; height: 338px; }
  .treatment-photo {
    position: absolute; inset: 0;
    background: linear-gradient(160deg, #5a4a44 0%, #7a625a 55%, #8f6f60 100%);
  }
  .treatment-details {
    position: absolute; left: 0; right: 0; text-align: center;
    color: var(--white); font-size: 17px; line-height: 23px;
  }
  .treatment--deep .treatment-details { top: 63px; }
  .treatment--thai .treatment-details { top: 117px; }
  .treatment-details .time { margin-top: 10px; }
  .treatment-details .price { font-weight: 700; }
  .treatment-details .gap { margin-top: 14px; }

  .label {
    position: absolute; height: 46px; border-radius: 10px;
    background: linear-gradient(180deg, var(--gold) 0%, var(--gold-deep) 100%);
    color: var(--ink); font-weight: 700; font-size: 18px; line-height: 46px; text-align: center;
  }
  .label--deep { left: 203px; width: 297px; top: 112px; }
  .label--thai { left: 156px; width: 393px; top: 508px; }

  .brand-name {
    position: absolute; left: 0; right: 0; top: 889px; text-align: center;
    color: var(--gold); font-size: 24px; font-family: "Raleway", sans-serif;
  }
  .contact {
    position: absolute; left: 0; right: 0; top: 922px; text-align: center;
    color: var(--white); font-size: 11px; font-weight: 700;
  }
  .contact span + span::before { content: "|"; margin: 0 18px; font-weight: 400; }
  .voucher-back {
    position: absolute; left: 0; right: 0; top: 940px; text-align: center;
    font-family: "Cinzel", serif; color: var(--gold); font-size: 32px;
  }
</style>
</head>
<body>

<section class="flyer flyer--front">
  <div class="hero-photo" role="img" aria-label="Photo of a woman relaxing while receiving a shoulder massage"></div>
  <svg class="shapes" viewBox="0 0 704 995" aria-hidden="true">
    <defs>
      <linearGradient id="goldBand" x1="0" y1="0" x2="1" y2="0">
        <stop offset="0" stop-color="#f3ea6e"/>
        <stop offset="0.55" stop-color="#f0c23c"/>
        <stop offset="1" stop-color="#e3951c"/>
      </linearGradient>
      <linearGradient id="orangeWedge" x1="0" y1="0" x2="1" y2="0">
        <stop offset="0" stop-color="#f0b230"/>
        <stop offset="1" stop-color="#e3951c"/>
      </linearGradient>
    </defs>
    <polygon points="0,378 178,440 0,468" fill="#f3ea6e"/>
    <polygon points="0,468 178,440 352,535 704,428 704,995 0,995" fill="#2f1b12"/>
    <polygon points="586,470 704,418 704,542" fill="url(#orangeWedge)"/>
    <polygon points="0,828 352,868 704,812 704,995 0,995" fill="url(#goldBand)"/>
  </svg>
  <h1 class="headline">Welcome<br>to Luxury</h1>
  <p class="intro intro--one">Set in the heart of Ashwell Green, Kolna Thai Massage will allow you to immerse yourself in a place where your wellbeing and rejuvenation is at the centre of what we do.</p>
  <p class="intro intro--two">Using Thai traditions, our highly trained therapists offer revitalising body treatments with their deep tissue massage techniques. In their hands, you will see and feel immediate results.</p>
  <h2 class="section-title">Massages</h2>
  <p class="intro intro--three">Restore balance. Revive your senses. Discover all the ways Kolna Thai Massage can breathe new life into your body and soul.</p>
  <p class="voucher-front">Gift Vouchers<br>Available</p>
</section>

<section class="flyer flyer--back">
  <h2 class="back-title">Massages</h2>

  <div class="treatment treatment--deep">
    <div class="treatment-photo" role="img" aria-label="Photo of a man receiving a deep tissue oil massage"></div>
    <div class="treatment-details">
      <p>Oil massage personalised, light<br>to firm pressure</p>
      <p class="time">60 MINUTES</p>
      <p class="price">£45</p>
      <p class="gap">Oil massage, medium<br>to firm pressure</p>
      <p>90 MINUTES</p>
      <p class="price">£55</p>
    </div>
  </div>
  <div class="label label--deep">DEEP TISSUE MASSAGE</div>

  <div class="treatment treatment--thai">
    <div class="treatment-photo" role="img" aria-label="Photo of a woman receiving a traditional Thai back massage"></div>
    <div class="treatment-details">
      <p>Dry massage, medium to firm<br>pressure applying stretching technique</p>
      <p class="time">60 MINUTES</p>
      <p class="price">£45</p>
    </div>
  </div>
  <div class="label label--thai">THAI FLOOR TRADTIONAL MASSAGE</div>

  <p class="brand-name">Kolna Thai Massage</p>
  <p class="contact"><span>0113 496 0127</span><span>www.kolnathaimassage.co.uk</span><span>14 Orchard Row Leeds LS8 9ZZ</span></p>
  <p class="voucher-back">Gift Vouchers Available</p>
</section>

</body>
</html>
```